Business Card

Just need business logo with phone number on it. 0472 318 506
And the following on the bottom of the card.

"Your local plumbing experts".
and emblems for Zarvo card, cheque and cash

```html
<!DOCTYPE html>
<html lang="en">
<head>
<meta charset="utf-8">
<title>Ridgeline Plumbing &amp; Drainage – Business Card</title>
<link href="https://fonts.googleapis.com/css2?family=Exo+2:wght@400;700;800&display=swap" rel="stylesheet">
<style>
  :root {
    --brand-red: #e8202e;
    --brand-blue: #1b8fd2;
    --ink: #1e1e1e;
    --paper: #ffffff;
    --backdrop: #d9d9d9;
  }
  * { margin: 0; padding: 0; box-sizing: border-box; }
  html, body {
    width: 1200px; height: 844px; overflow: hidden;
    background: var(--backdrop);
    font-family: "Exo 2", Arial, sans-serif;
  }
  .stage { position: relative; width: 1200px; height: 844px; }
  .card {
    position: absolute; top: 268px;
    width: 540px; height: 309px;
    overflow: hidden;
    box-shadow: 0 6px 18px rgba(0,0,0,.18);
  }
  /* Front */
  .card-front { left: 45px; background: var(--paper); }
  .brand-name {
    position: absolute; top: 38px; right: 60px;
    color: var(--brand-red); font-weight: 800;
    text-align: center; line-height: 1;
  }
  .brand-name .mono { display: block; font-size: 54px; letter-spacing: 1px; }
  .brand-name .full { display: block; font-size: 15px; letter-spacing: 1.5px; margin-top: 6px; }
  .edge-mark { position: absolute; left: 0; width: 8px; height: 26px; }
  .edge-mark.red { top: 186px; background: var(--brand-red); }
  .edge-mark.blue { top: 250px; background: var(--brand-blue); }
  .phone-line {
    position: absolute; left: 26px; top: 184px;
    display: flex; align-items: center; gap: 10px;
    font-size: 23px; color: var(--ink);
  }
  .phone-icon { width: 28px; height: 28px; }
  .tagline {
    position: absolute; left: 26px; top: 246px;
    font-size: 23px; color: var(--ink);
  }
  .payments {
    position: absolute; right: 28px; top: 168px;
    display: flex; align-items: center; gap: 10px;
  }
  .pay-card {
    width: 66px; height: 38px; border: 2px solid var(--brand-blue); border-radius: 4px;
    display: flex; align-items: center; justify-content: center;
    color: var(--brand-blue); font-weight: 700; font-size: 17px;
  }
  .pay-icon { width: 66px; height: 38px; }
  /* Back */
  .card-back { left: 615px; background: var(--brand-red); }
  .card-back .stripe {
    position: absolute; left: 0; bottom: 0; width: 100%; height: 14px;
    background: var(--brand-blue);
  }
  .back-name {
    position: absolute; left: 0; right: 0; top: 112px;
    text-align: center; color: var(--paper);
    font-weight: 800; font-size: 64px; letter-spacing: 2px; line-height: 1;
  }
</style>
</head>
<body>
<main class="stage">
  <section class="card card-front" aria-label="Business card front">
    <div class="brand-name">
      <span class="mono">RPD</span>
      <span class="full">RIDGELINE PLUMBING<br>&amp; DRAINAGE</span>
    </div>

    <span class="edge-mark red"></span>
    <div class="phone-line">
      <svg class="phone-icon" viewBox="0 0 28 28" aria-hidden="true">
        <circle cx="14" cy="14" r="12.5" fill="none" stroke="#e8202e" stroke-width="2.5"/>
        <path d="M8 11c0-2 2-3 6-3s6 1 6 3l-2 1-1-2h-6l-1 2z M10 13h8l1 6H9z" fill="#1b8fd2"/>
      </svg>
      <span>0472 318 506</span>
    </div>

    <div class="payments" aria-label="Accepted payments">
      <div class="pay-card">Zarvo</div>
      <svg class="pay-icon" viewBox="0 0 66 38" aria-label="Cash">
        <rect x="1" y="1" width="64" height="36" rx="3" fill="#111"/>
        <circle cx="33" cy="19" r="9" fill="#fff"/>
        <text x="33" y="24" text-anchor="middle" font-family="Arial, sans-serif" font-weight="700" font-size="13" fill="#111">$</text>
      </svg>
      <svg class="pay-icon" viewBox="0 0 66 38" aria-label="Cheque">
        <rect x="2" y="3" width="62" height="32" rx="2" fill="#fff" stroke="#222" stroke-width="2"/>
        <line x1="8" y1="12" x2="30" y2="12" stroke="#222" stroke-width="2"/>
        <line x1="8" y1="20" x2="40" y2="20" stroke="#222" stroke-width="1.5"/>
        <line x1="36" y1="28" x2="58" y2="28" stroke="#222" stroke-width="1.5"/>
        <rect x="46" y="9" width="12" height="7" fill="none" stroke="#222" stroke-width="1.5"/>
      </svg>
    </div>

    <span class="edge-mark blue"></span>
    <p class="tagline">Your local plumbing experts</p>
  </section>

  <section class="card card-back" aria-label="Business card back">
    <div class="back-name">RPD</div>
    <span class="stripe"></span>
  </section>
</main>
</body>
</html>
```